Walk Boldly into Morning: 48 Days to a Year of Courage and Calm

This is a non-fiction, self-help book. The first edition was published a decade ago, and it needs a new design. Nothing too literal (no actual hearts on the cover) but something inspirational or perhaps something quite plain. The current cover is below for reference, but I DO NOT want something similar to that. It is outdated.

The cover must include:

1. Title: Walk Boldly into Morning
2. Subtitle: 48 Days to a Year of Courage and Calm
3. Author Name: Dean Forsythe

It should also have plenty of "white space" in other words the fonts shouldnt be so big that they take up the whole cover.

Dimensions: 9" x 6.25"

Target Market(s)

adults interested in personal development

Font styles to use
Serif
Script

Colors

Designer to choose colors to be used in the design.

Requirements
Must have
• Classic look and feel. The current design is too busy. I have included examples of the style I like below. I'm open to a singular graphic/photo but nothing more than that. Probably plain text is best.
• Please look at the samples I have included of best-selling books in the genre that I like. The cover should be modeled after these.

```html
<!DOCTYPE html>
<html lang="en">
<head>
<meta charset="UTF-8">
<title>Walk Boldly into Morning — Dean Forsythe</title>
<link rel="stylesheet" href="https://fonts.googleapis.com/css2?family=Abril+Fatface&display=swap">
<style>
  :root {
    --teal: #187e71;
    --sea: #13718a;
    --indigo: #2f4a9e;
    --ink: #1f1e1c;
    --paper: #ffffff;
  }
  html, body {
    margin: 0;
    padding: 0;
    width: 833px;
    height: 1200px;
    overflow: hidden;
  }
  .cover {
    position: relative;
    width: 833px;
    height: 1200px;
    background: linear-gradient(90deg, var(--teal) 0%, var(--sea) 55%, var(--indigo) 100%);
    font-family: "Abril Fatface", "Playfair Display", Georgia, serif;
    color: var(--paper);
    overflow: hidden;
  }
  .title {
    position: absolute;
    left: 165px;
    top: 170px;
    margin: 0;
    font-weight: 400;
    font-size: 116px;
    line-height: 137px;
    letter-spacing: -2px;
  }
  .title span { display: block; }
  .subtitle {
    position: absolute;
    left: 167px;
    top: 966px;
    margin: 0;
    font-size: 37px;
    line-height: 52px;
    font-weight: 400;
    letter-spacing: -0.3px;
  }
  .author-band {
    position: absolute;
    left: 688px;
    top: 376px;
    width: 145px;
    height: 448px;
    background: var(--ink);
    display: flex;
    align-items: center;
    justify-content: center;
  }
  .author {
    margin: 0;
    writing-mode: vertical-rl;
    transform: rotate(180deg);
    font-size: 58px;
    line-height: 1;
    font-weight: 400;
    white-space: nowrap;
  }
</style>
</head>
<body>
  <main class="cover">
    <h1 class="title">
      <span>Walk</span>
      <span>Boldly</span>
      <span>into</span>
      <span>Morning</span>
    </h1>
    <p class="subtitle">48 Days to a Year of<br>Courage and Calm</p>
    <div class="author-band">
      <p class="author">Dean Forsythe</p>
    </div>
  </main>
</body>
</html>
```